Billboard design for retail kitchen cabinet business

We have a large 7,000 square-foot showroom of beautiful kitchen cabinet displays of all different designs and price ranges. In business for over 50 years with expert designers.
Full size Norvale Media 14' X 48' billboard
Target Market(s)
Retail public on high traffic Los Angeles streets

```html
<!DOCTYPE html>
<html lang="en">
<head>
<meta charset="utf-8">
<title>Cabinet Hall Billboard</title>
<link rel="stylesheet" href="https://fonts.googleapis.com/css2?family=Oswald:wght@600&family=Poppins:wght@700&display=swap">
<style>
  :root {
    --frame: #3a3a3c;
    --paper: #ffffff;
    --gold: #fbb316;
    --gold-soft: #fde27a;
    --grey-text: #a7a9ab;
    --grey-band: #e4e4e5;
    --photo-dark: #5a5658;
    --photo-warm: #b8743e;
    --photo-green: #a7ad6a;
  }
  html, body {
    margin: 0;
    padding: 0;
    overflow: hidden;
    background: var(--frame);
  }
  .billboard {
    position: relative;
    width: 1200px;
    height: 418px;
    background: var(--frame);
    overflow: hidden;
  }
  .billboard__face {
    position: absolute;
    left: 47px;
    top: 47px;
    width: 1106px;
    height: 323px;
    background: var(--paper);
    overflow: hidden;
  }
  .billboard__art {
    position: absolute;
    inset: 0;
  }
  .brand-name {
    position: absolute;
    left: 164px;
    top: 62px;
    margin: 0;
    font-family: "Oswald", "Arial Narrow", sans-serif;
    font-weight: 600;
    font-size: 86px;
    line-height: 80px;
    letter-spacing: -1px;
    color: var(--gold);
    text-transform: uppercase;
  }
  .brand-name span { display: block; }
  .web-address {
    position: absolute;
    left: 56px;
    top: 265px;
    margin: 0;
    font-family: "Poppins", "Arial", sans-serif;
    font-weight: 700;
    font-size: 40px;
    letter-spacing: -0.5px;
    color: var(--grey-text);
  }
</style>
</head>
<body>
  <div class="billboard">
    <div class="billboard__face">
      <svg class="billboard__art" width="1106" height="323" viewBox="0 0 1106 323" aria-hidden="false">
        <defs>
          <linearGradient id="swoosh-fill" x1="0" y1="0" x2="1" y2="0">
            <stop offset="0" stop-color="var(--gold-soft)" stop-opacity="0.9"/>
            <stop offset="0.45" stop-color="var(--gold-soft)" stop-opacity="0.55"/>
            <stop offset="1" stop-color="var(--gold-soft)" stop-opacity="0.15"/>
          </linearGradient>
          <linearGradient id="band-fill" x1="0" y1="0" x2="1" y2="1">
            <stop offset="0" stop-color="#f1f1f2"/>
            <stop offset="1" stop-color="var(--grey-band)"/>
          </linearGradient>
          <linearGradient id="photo-dark-fill" x1="0" y1="0" x2="1" y2="1">
            <stop offset="0" stop-color="#cfcfcf"/>
            <stop offset="0.5" stop-color="var(--photo-dark)"/>
            <stop offset="1" stop-color="#2f2c2e"/>
          </linearGradient>
          <linearGradient id="photo-warm-fill" x1="0" y1="0" x2="0" y2="1">
            <stop offset="0" stop-color="#e9dcc2"/>
            <stop offset="1" stop-color="var(--photo-warm)"/>
          </linearGradient>
          <linearGradient id="photo-green-fill" x1="0" y1="0" x2="0" y2="1">
            <stop offset="0" stop-color="#d9cf9c"/>
            <stop offset="1" stop-color="var(--photo-green)"/>
          </linearGradient>
        </defs>

        <path class="swoosh" d="M0 148 C120 170 260 175 380 160 C480 145 560 100 555 0 L575 0 C600 120 520 215 380 250 C250 280 90 270 0 238 Z" fill="url(#swoosh-fill)"/>
        <path class="swoosh-edge" d="M0 232 C120 262 260 268 380 242 C500 215 560 160 570 90" fill="none" stroke="var(--gold)" stroke-opacity="0.55" stroke-width="5"/>

        <polygon class="grey-band" points="553,0 1106,0 1106,323 870,323" fill="url(#band-fill)"/>

        <path class="photo photo--dark-kitchen" role="img" aria-label="Photo of a modern kitchen with dark island, white counters and glass-front cabinets"
              d="M575 0 L1106 0 L1106 44 L860 302 Q838 322 815 302 Z" fill="url(#photo-dark-fill)"/>
        <polygon class="photo photo--wood-kitchen" role="img" aria-label="Photo of a warm wood kitchen island with a bowl of apples"
                 points="505,323 666,154 846,323" fill="url(#photo-warm-fill)"/>
        <polygon class="photo photo--green-kitchen" role="img" aria-label="Photo of a sage green kitchen with tiled backsplash and pendant lamp"
                 points="873,323 994,205 1106,312 1106,323" fill="url(#photo-green-fill)"/>
      </svg>

      <h1 class="brand-name"><span>Cabinet</span><span>Hall</span></h1>
      <p class="web-address">cabinethall.net</p>
    </div>
  </div>
</body>
</html>
```